Welding and farication business card

Business name Tbm Welding & Fabrication

I need a business card made for my welding and fabrication business that is bold and stands out. My business is both welding repairs on machinery and anything else you can imagine as well as fabricating new products. i have used this service before and was very happy with the out come of my design logo. i think the card should remain fairly simple and classy but also be bold. I think a black card would best be suited to the talk with my logo on it. i feel the back of the card should just have my logo and the front have my logo email, website and phone number and maybe incorporate a facebook and instagram simple if it can be made look good these arnt a necessity.
I have included both my logo and some business card ideas below

Target Market(s)

Farmers, heavy industry, earthmoving, trucking

Industry/Entity Type

Engineering

Contact Information for Business Card

0438517264
dale@tbmweldingandfabrication.com.au
www.tbmweldingandfabrication.com.au

Colors
33a6d7
0255a3

Requirements
Must have
• Dale Hutchins
my phone number 0438517264
my logo
Preferably a black card desgn
Nice to have
• List of what i do,
Sheds and carports
Ute trays
Stockyards
Trailers
Farm equipment
Stockcrates
Gateways and Entrances
Breakdowns
Maintenance
And lots more!

```html
<!DOCTYPE html>
<html lang="en">
<head>
<meta charset="utf-8">
<title>TBM Welding &amp; Fabrication – Business Card</title>
<link href="https://fonts.googleapis.com/css2?family=Lato:ital,wght@0,400;0,700;0,900;1,900&display=swap" rel="stylesheet">
<style>
  :root {
    --stage: #cbcbcb;
    --card: #050608;
    --brand-blue: #0255a3;
    --spark-blue: #33a6d7;
    --white: #ffffff;
    --ink: #1b1b1b;
  }
  * { box-sizing: border-box; margin: 0; padding: 0; }
  html, body {
    width: 1200px; height: 1200px; overflow: hidden;
    background: var(--stage);
    font-family: "Lato", Arial, sans-serif;
  }
  .canvas { position: relative; width: 1200px; height: 1200px; }

  .card {
    position: absolute; left: 240px; width: 720px; height: 420px;
    background: var(--card); border-radius: 36px; overflow: hidden;
    box-shadow: 0 6px 14px rgba(0,0,0,.28);
    color: var(--white);
  }
  .card--front { top: 142px; }
  .card--back { top: 638px; }

  /* Brand name lockup */
  .brand { position: absolute; display: flex; align-items: center; gap: 14px; color: var(--white); font-weight: 900; }
  .brand__dot { border-radius: 50%; background: var(--spark-blue); flex: none; }
  .brand__text { display: flex; flex-direction: column; line-height: 1; }
  .brand__main { letter-spacing: 3px; }
  .brand__sub { letter-spacing: .5px; margin-top: 8px; }

  .card--front .brand { left: 48px; top: 74px; }
  .card--front .brand__dot { width: 22px; height: 22px; }
  .card--front .brand__main { font-size: 64px; }
  .card--front .brand__sub { font-size: 17px; }

  .card--back .brand { left: 50%; top: 84px; transform: translateX(-50%); }
  .card--back .brand__dot { width: 34px; height: 34px; }
  .card--back .brand__main { font-size: 104px; }
  .card--back .brand__sub { font-size: 27px; margin-top: 12px; }

  /* Name tab */
  .name-tab {
    position: absolute; left: 0; top: 204px; width: 297px; height: 78px;
    background: var(--white); border-radius: 0 39px 39px 0;
    padding: 14px 0 0 47px; color: var(--ink);
  }
  .name-tab__name { font-size: 31px; font-weight: 900; color: var(--brand-blue); line-height: 1; white-space: nowrap; }
  .name-tab__role { font-size: 19px; font-weight: 400; margin-top: 4px; }

  /* Contacts */
  .contacts { position: absolute; left: 48px; top: 308px; list-style: none; }
  .contacts__item { display: flex; align-items: center; height: 29px; font-size: 18px; }
  .contacts__icon { width: 20px; height: 20px; margin-right: 17px; flex: none; }

  /* Torch artwork area */
  .torch-art {
    position: absolute; left: 420px; top: 0; width: 290px; height: 352px;
    background: radial-gradient(circle at 78% 28%, rgba(51,166,215,.55), rgba(51,166,215,.12) 30%, transparent 55%),
                linear-gradient(200deg, rgba(255,255,255,.14), rgba(2,85,163,.25) 80%, transparent);
    border-radius: 0 36px 0 0;
  }

  .social { position: absolute; left: 476px; top: 365px; display: flex; align-items: center; gap: 12px; font-size: 19px; }
  .social__dot { width: 22px; height: 22px; border-radius: 50%; border: 2px solid var(--spark-blue); }

  /* Services */
  .services { position: absolute; left: 0; right: 0; top: 303px; text-align: center; font-size: 19.5px; line-height: 29px; }
</style>
</head>
<body>
<main class="canvas">

  <section class="card card--front" aria-label="Card front">
    <div class="brand">
      <span class="brand__dot"></span>
      <span class="brand__text">
        <span class="brand__main">TBM</span>
        <span class="brand__sub">WELDING &amp; FABRICATION</span>
      </span>
    </div>

    <div class="name-tab">
      <p class="name-tab__name">DALE HUTCHINS</p>
      <p class="name-tab__role">Director</p>
    </div>

    <ul class="contacts">
      <li class="contacts__item">
        <svg class="contacts__icon" viewBox="0 0 20 20" fill="none" stroke="#33a6d7" stroke-width="1.8" stroke-linejoin="round">
          <path d="M4 2.5l3 .5 1 4-2 1.5c1 2.3 2.5 3.8 4.5 4.5L12 11l4 1 .5 3c-.5 1.5-2 2.5-3.5 2.2C8 16 4 12 2.8 6.5 2.5 4.8 3 3.2 4 2.5z"/>
          <path d="M12 3a5 5 0 0 1 5 5M12 6a2 2 0 0 1 2 2" stroke-linecap="round"/>
        </svg>
        0438 517 264
      </li>
      <li class="contacts__item">
        <svg class="contacts__icon" viewBox="0 0 20 20">
          <rect x="1" y="4" width="18" height="12" rx="1" fill="#33a6d7"/>
          <path d="M1.5 4.5L10 11l8.5-6.5M1.5 15.5l6-5.5M18.5 15.5l-6-5.5" stroke="#050608" stroke-width="1.4" fill="none"/>
        </svg>
        dale@tbmweldingandfabrication.com.au
      </li>
      <li class="contacts__item">
        <svg class="contacts__icon" viewBox="0 0 20 20" fill="none" stroke="#33a6d7" stroke-width="1.5">
          <circle cx="10" cy="10" r="8"/>
          <ellipse cx="10" cy="10" rx="3.5" ry="8"/>
          <path d="M2 10h16M3.5 6h13M3.5 14h13"/>
        </svg>
        www.tbmweldingandfabrication.com.au
      </li>
    </ul>

    <div class="torch-art" role="img" aria-label="White welding torch illustration with a bright blue spark at its tip and a blue cable"></div>

    <div class="social">
      <span class="social__dot"></span>
      <span>@TbmWelding</span>
    </div>
  </section>

  <section class="card card--back" aria-label="Card back">
    <div class="brand">
      <span class="brand__dot"></span>
      <span class="brand__text">
        <span class="brand__main">TBM</span>
        <span class="brand__sub">WELDING &amp; FABRICATION</span>
      </span>
    </div>

    <p class="services">
      Sheds and carports &nbsp;|&nbsp; Ute trays &nbsp;|&nbsp; Stockyards &nbsp;|&nbsp; Trailers<br>
      Farm equipment &nbsp;|&nbsp; StockcratesGateways and Entrances<br>
      Breakdowns &nbsp;|&nbsp; Maintenance
    </p>
  </section>

</main>
</body>
</html>
```